I need a business card/logo designed that obviously describes my business. We are a residential appraisal and home inspection company in Springfield, MO. We offer residential appraisals, home inspection, pest inspection and radon gas measurement. We have been in business for 18 years and hold state certified residential appraisal licenses and DRUMI certified home inspection licenses. I have a logo that I really like and will attach, but would be open to new suggestions. I like more modern designs than traditional and would like a two sided card with our services, licenses and qualifications on the back.

```html
<!DOCTYPE html>
<html lang="en">
<head>
<meta charset="utf-8">
<title>Larkvale Dwelling Review – Business Card</title>
<link rel="stylesheet" href="https://fonts.googleapis.com/css2?family=Source+Sans+3:wght@400;600&display=swap">
<style>
  :root {
    --gold: #eaa627;
    --brown: #9c7c48;
    --grey: #8c8c8c;
    --card: #fbfbfb;
    --stage: #e9e6e1;
    --social: #c9c4bb;
  }
  * { margin: 0; padding: 0; box-sizing: border-box; }
  html, body { width: 1200px; height: 780px; overflow: hidden; }
  body {
    background: var(--stage);
    font-family: "Source Sans 3", "Myriad Pro", sans-serif;
    display: flex; align-items: center; justify-content: center; gap: 40px;
  }
  .card {
    position: relative; width: 540px; height: 309px;
    background: var(--card); border-radius: 16px;
    box-shadow: 0 4px 14px rgba(0,0,0,.12);
    overflow: hidden;
  }
  .brand { display: flex; align-items: center; gap: 10px; }
  .brand-mark { width: 14px; height: 14px; background: var(--gold); flex: none; }
  .brand-name { color: var(--brown); font-weight: 600; font-size: 25px; line-height: 1.1; white-space: nowrap; }
  .rule { position: absolute; height: 1px; background: var(--gold); }

  /* front */
  .social { position: absolute; right: 34px; top: 22px; display: flex; gap: 7px; }
  .social span { width: 16px; height: 16px; background: var(--social); border-radius: 2px; }
  .front .brand { position: absolute; left: 34px; top: 70px; }
  .front .rule { left: 34px; top: 160px; width: 330px; }
  .person { position: absolute; right: 34px; top: 112px; text-align: right; }
  .person-name { color: var(--brown); font-size: 21px; font-weight: 600; line-height: 1.1; }
  .person-role { color: var(--gold); font-size: 13px; line-height: 1.3; }
  .address { position: absolute; right: 34px; top: 196px; text-align: right;
    color: var(--brown); font-size: 14px; line-height: 1.35; }
  .contact { position: absolute; left: 40px; top: 184px; color: var(--grey); font-size: 14px; line-height: 1.45; }
  .contact li { list-style: none; display: flex; align-items: center; gap: 8px; }
  .contact svg { width: 12px; height: 12px; flex: none; }
  .contact .web { color: var(--gold); }

  /* back */
  .back .brand { position: absolute; left: 0; right: 0; top: 60px; justify-content: center; }
  .back .rule { left: 130px; top: 100px; width: 280px; }
  .services { position: absolute; left: 0; right: 0; top: 124px; text-align: center; }
  .services-title { color: var(--gold); font-size: 15px; font-weight: 600; letter-spacing: .4px; margin-bottom: 6px; }
  .services p { color: var(--brown); font-size: 14px; line-height: 1.4; }
</style>
</head>
<body>
  <section class="card front">
    <div class="social" aria-label="Social links">
      <span></span><span></span><span></span><span></span>
    </div>
    <div class="brand">
      <span class="brand-mark"></span>
      <span class="brand-name">Larkvale Dwelling Review</span>
    </div>
    <div class="rule"></div>
    <div class="person">
      <div class="person-name">Employee Name</div>
      <div class="person-role">Managing Director</div>
    </div>
    <div class="address">000 Abcdefgh Rd.,<br>Suite 000 Fernwick, USA</div>
    <ul class="contact">
      <li><svg viewBox="0 0 12 12"><rect width="12" height="12" rx="2" fill="#eaa627"/><path d="M3 3h2l1 2-1 1a5 5 0 0 0 1 1l1-1 2 1v2a6 6 0 0 1-6-6z" fill="#fff"/></svg>000.000.0000</li>
      <li><svg viewBox="0 0 12 12"><rect width="12" height="12" rx="2" fill="#eaa627"/><rect x="3" y="4" width="6" height="5" fill="#fff"/></svg>000.000.0000</li>
      <li><svg viewBox="0 0 12 12"><rect width="12" height="12" rx="2" fill="#eaa627"/><path d="M2.5 3.5h7v5h-7z M2.5 3.5l3.5 3 3.5-3" fill="none" stroke="#fff"/></svg>larkvale@youremail.com</li>
      <li class="web">www.yourwebsite.com</li>
    </ul>
  </section>

  <section class="card back">
    <div class="brand">
      <span class="brand-mark"></span>
      <span class="brand-name">Larkvale Dwelling Review</span>
    </div>
    <div class="rule"></div>
    <div class="services">
      <div class="services-title">OUR SERVICES</div>
      <p>residential appraisals / home inspection / pest inspection</p>
      <p>radon gas measurement</p>
      <p>We have been in business for 18 years and<br>hold state certified residential<br>appraisal licenses and DRUMI certified home inspection licenses</p>
    </div>
  </section>
</body>
</html>
```